Candle company needs a label for candle

Looking for a designer to create my candle label. I am going to attach a few pictures of my vision for the label as well as my Company Logo and jar I have puchased. I'm going for the modern rustic feel but you are the designer and have full trust in your abilities. The label is going to be printed on Kraft paper (2x3) so looking for the font to be black. The candle label MUST include the following information:
Candle Birchway Co.
NO. 01: Eucalyptus + Spearmint
Handmade In NJ
Soy Wax
9oz

Industry/Entity Type

Candle Industry

Colors

Designer to choose colors to be used in the design.

Requirements
Should not have
• Any images

```html
<!DOCTYPE html>
<html lang="en">
<head>
<meta charset="utf-8">
<title>Candle Birchway Co. – No. 01 Eucalyptus + Spearmint Label</title>
<link rel="stylesheet" href="https://fonts.googleapis.com/css2?family=Crimson+Text:wght@400&display=swap">
<style>
  :root {
    --page: #f4f1ee;
    --kraft: #c6a491;
    --ink: #1e1a17;
  }
  html, body {
    margin: 0;
    padding: 0;
    width: 1156px;
    height: 1200px;
    overflow: hidden;
    background: var(--page);
  }
  .label {
    position: absolute;
    left: 58px;
    top: 254px;
    width: 1040px;
    height: 693px;
    background: var(--kraft);
    color: var(--ink);
    font-family: "Crimson Text", "Times New Roman", serif;
  }
  .brand-name {
    position: absolute;
    left: 0;
    right: 0;
    top: 190px;
    margin: 0;
    text-align: center;
    font-family: "Crimson Text", "Times New Roman", serif;
    font-weight: 400;
    font-size: 44px;
    line-height: 1;
    color: var(--ink);
  }
  .scent-table {
    position: absolute;
    left: 235px;
    top: 355px;
    width: 599px;
    height: 137px;
    border: 2px solid var(--ink);
    box-sizing: border-box;
    display: flex;
  }
  .scent-table .cell {
    display: flex;
    align-items: center;
    justify-content: center;
    box-sizing: border-box;
  }
  .scent-table .cell + .cell {
    border-left: 2px solid var(--ink);
  }
  .cell.number-label {
    width: 96px;
    font-size: 30px;
  }
  .cell.number-label sup {
    font-size: 18px;
    vertical-align: 10px;
  }
  .cell.number {
    width: 115px;
    font-size: 68px;
  }
  .cell.scent-name {
    flex: 1;
    flex-direction: column;
    font-size: 34px;
    line-height: 1.05;
    text-align: center;
  }
  .details {
    position: absolute;
    left: 235px;
    width: 599px;
    top: 506px;
    display: flex;
    justify-content: space-between;
    padding: 0 20px;
    box-sizing: border-box;
    font-size: 28px;
  }
  .details .material {
    text-transform: uppercase;
    letter-spacing: 0.02em;
  }
  .net-weight {
    position: absolute;
    left: 0;
    right: 0;
    top: 600px;
    text-align: center;
    font-size: 30px;
  }
</style>
</head>
<body>
  <section class="label" aria-label="Candle label">
    <h1 class="brand-name">Candle Birchway Co.</h1>

    <div class="scent-table">
      <div class="cell number-label">N<sup>o</sup></div>
      <div class="cell number">01</div>
      <div class="cell scent-name">
        <span>Eucalyptus</span>
        <span>+</span>
        <span>Spearmint</span>
      </div>
    </div>

    <div class="details">
      <span class="origin">Handmade in NJ</span>
      <span class="material">Soy Wax</span>
    </div>

    <div class="net-weight">9oz</div>
  </section>
</body>
</html>
```